Organic Food Producer Needs Business Card

We need an attractive business card that is both trendy and professional. We are a FQIB, Non Gmo Certified organic producer of coconut oil, coconut flour and additional cacao products. We produce some of the world's purest coconut oil and coconut oil derived products in the world.
We take pride in the purity of our products and the transparency with which we create our products. Use of FQIB Organic and Non GMO logos is acceptable and preferred. The final design would reflect our values for purity and the natural state of our products.
The business card should include: job title, email address, phone number and facebook, twitter, instagram tag.
Don't be afraid to get creative! I have attached some of our packaging design in JPG format as well as our logo. The jpgs dont display the colors correctly in chrome but they will display correctly if you DL and open them in photoshop.
Target Market(s)
Cards likely to be used in organic food industry events for people such as buyers, trade show reps, etc... but also store owners and people casually interested in.
The company's target market :
Primary:
Women - 22-65. Women typically hold the household budget and make the purchasing decisions at the supermarket. They are interested in quality healthy and beauty products at a good value. Organic, fair trade, artisanally made are all important attributes of brands they purchase. They try to maintain a healthy lifestyle through proper eating, exercise and work/life balance.
Secondary:
Men - 44% of American adults are single so it is important to note that men will also be a key target audience. And they too are concerned and passionate about organic, fair trade, artisanally made, good value and living a healthy lifestyle.
Tertiary:
Health & Wellness Professionals (Nutritionists, Doctors, etc) Coconut is highly nutritional and more and more, it is being recommended as part of a healthy diet by professionals. We should keep this audience in mind as well, particularly when we build a website with useful resources such as the company’s high standards, the health benefits of coconut, nutrition info and recipes.
Industry/Entity Type
Business
Requirements
Must have
- Pretty open minded about creativity and variety, I do like the color palettes in the labeling files provided... but it is not a deal breaker to vary from this.
Should be visually impacting.
Nice to have
- Would like to have some creative use of raised lettering or detail.
Should not have
- Although the company is based in the caribbean, we are not looking for an overly ethnic caribbean feel.
You should open the attached files in photoshop, as they seem to distort the color in a web browser.

```html
<!DOCTYPE html>
<html lang="en">
<head>
<meta charset="utf-8">
<title>Coral Grove – Business Card</title>
<link href="https://fonts.googleapis.com/css2?family=Open+Sans:wght@400;600;700&display=swap" rel="stylesheet">
<style>
  :root {
    --backdrop: #e9e4dc;
    --card: #000000;
    --teal: #0a8fab;
    --cream: #f4e4c6;
    --white: #ffffff;
  }
  html, body {
    margin: 0;
    padding: 0;
    width: 1130px;
    height: 1200px;
    overflow: hidden;
    background: var(--backdrop);
    font-family: "Open Sans", sans-serif;
  }
  .canvas {
    position: relative;
    width: 1130px;
    height: 1200px;
  }
  .card {
    position: absolute;
    width: 897px;
    height: 514px;
  }
  .card--front { left: 113px; top: 70px; }
  .card--back  { left: 108px; top: 630px; }
  .card__shape {
    position: absolute;
    inset: 0;
    width: 897px;
    height: 514px;
  }
  .card__shape path { fill: var(--card); }

  .brand {
    position: absolute;
    left: 64px;
    top: 92px;
  }
  .brand__row {
    display: flex;
    align-items: center;
    gap: 16px;
  }
  .brand__dot {
    width: 44px;
    height: 44px;
    border-radius: 50%;
    background: var(--teal);
  }
  .brand__name {
    color: var(--teal);
    font-weight: 600;
    font-size: 54px;
    line-height: 1;
    letter-spacing: 1px;
  }
  .brand__tagline {
    margin: 12px 0 0 60px;
    color: var(--cream);
    font-size: 19px;
    letter-spacing: 1px;
  }

  .address {
    position: absolute;
    left: 64px;
    top: 264px;
    margin: 0;
    color: var(--white);
    font-size: 21px;
  }
  .contacts {
    position: absolute;
    left: 64px;
    top: 306px;
    margin: 0;
    padding: 0;
    list-style: none;
  }
  .contacts li {
    display: flex;
    align-items: center;
    gap: 10px;
    height: 33px;
    color: var(--white);
    font-size: 21px;
  }
  .contacts svg {
    width: 22px;
    height: 22px;
    fill: var(--cream);
    stroke: var(--cream);
  }
  .contacts__label {
    color: var(--cream);
  }

  .person {
    position: absolute;
    right: 102px;
    top: 356px;
    text-align: right;
  }
  .person__name {
    margin: 0;
    color: var(--teal);
    font-weight: 600;
    font-size: 28px;
    line-height: 1.2;
  }
  .person__title {
    margin: 2px 0 0;
    color: var(--cream);
    font-size: 22px;
  }

  .back__brand {
    position: absolute;
    left: 0;
    right: 0;
    top: 150px;
    display: flex;
    justify-content: center;
    align-items: center;
    gap: 22px;
  }
  .back__dot {
    width: 64px;
    height: 64px;
    border-radius: 50%;
    background: var(--teal);
  }
  .back__name {
    color: var(--teal);
    font-weight: 600;
    font-size: 84px;
    line-height: 1;
    letter-spacing: 1px;
  }
  .back__web {
    position: absolute;
    left: 0;
    right: 0;
    top: 438px;
    margin: 0;
    text-align: center;
    color: var(--white);
    font-weight: 700;
    font-size: 30px;
    letter-spacing: 5px;
  }
</style>
</head>
<body>
<main class="canvas">

  <section class="card card--front">
    <svg class="card__shape" viewBox="0 0 897 514" aria-hidden="true">
      <path d="M42,0 H855 A42,42 0 0 0 897,42 V472 A42,42 0 0 0 855,514 H42 A42,42 0 0 0 0,472 V42 A42,42 0 0 0 42,0 Z"/>
    </svg>

    <div class="brand">
      <div class="brand__row">
        <span class="brand__dot"></span>
        <span class="brand__name">coral grove</span>
      </div>
      <p class="brand__tagline">handcrafted in the caribbean</p>
    </div>

    <p class="address">Street Name, City Name, Zip Code-00000</p>

    <ul class="contacts">
      <li>
        <svg viewBox="0 0 24 24" aria-hidden="true"><circle cx="12" cy="12" r="10" fill="none" stroke-width="2"/><path d="M9 6c-1 1-1.5 3 0 6s4 5 6 5l1.5-1.5-2-2-1.5 1c-1-.5-2.5-2-3-3.5l1-1.5-2-2z" stroke="none"/></svg>
        012-345-6789
      </li>
      <li>
        <svg viewBox="0 0 24 24" aria-hidden="true"><rect x="7" y="2" width="10" height="7" stroke="none"/><rect x="2" y="10" width="20" height="8" rx="1" stroke="none"/><rect x="6" y="16" width="12" height="6" stroke="none"/></svg>
        012-345-6789
      </li>
      <li>
        <svg viewBox="0 0 24 24" aria-hidden="true"><path d="M2 9 L12 3 L22 9 V21 H2 Z" stroke="none"/><path d="M3 10 L12 16 L21 10" fill="none" stroke="#000" stroke-width="1.6"/></svg>
        info@coralgrove.com
      </li>
      <li>
        <svg viewBox="0 0 24 24" aria-hidden="true"><circle cx="12" cy="12" r="10" fill="none" stroke-width="1.6"/><ellipse cx="12" cy="12" rx="4.5" ry="10" fill="none" stroke-width="1.4"/><path d="M2 12 H22 M4 7 H20 M4 17 H20" fill="none" stroke-width="1.4"/></svg>
        www.coralgrove.com
      </li>
      <li>
        <svg viewBox="0 0 24 24" aria-hidden="true"><path d="M3 4 H21 V16 H10 L5 21 V16 H3 Z" stroke="none"/></svg>
        <span class="contacts__label">fb / tw / ig</span> @coralgrove
      </li>
    </ul>

    <div class="person">
      <p class="person__name">Your Name</p>
      <p class="person__title">Title</p>
    </div>
  </section>

  <section class="card card--back">
    <svg class="card__shape" viewBox="0 0 897 514" aria-hidden="true">
      <path d="M42,0 H855 A42,42 0 0 0 897,42 V472 A42,42 0 0 0 855,514 H42 A42,42 0 0 0 0,472 V42 A42,42 0 0 0 42,0 Z"/>
    </svg>
    <div class="back__brand">
      <span class="back__dot"></span>
      <span class="back__name">coral grove</span>
    </div>
    <p class="back__web">www.coralgrove.com</p>
  </section>

</main>
</body>
</html>
```